New Hotel Showcase Website

We plan to launch a website called www.brindlestays.net which showcases the world’s best new hotels. We want a mock up for 2 pages: the homepage (page 1) and the individual hotel page (page 2). We are looking for a design which combines simplicity while highlighting images/features of the hotel. Because the theme of the site is new hotels it is important that the design somehow emphasizes the age of each hotel listed – both on the homepage and then on the individual hotel page.

NOTE: WE WANT A CREATIVE, NEW APPROACH TO DISPLAYING HOTELS. NOT JUST A COPY OF CURRENT HOTEL WEBSITES.

The design should consider unique and creative ways of helping users to navigate the homepage (page 1) based on the age, location or style of the hotel they are interested in. The individual hotel page(page 2) can be more standard by clearly setting out hotel photos, feature lists, reviews, contact details and potential discounts. There is no booking system needed as this is not a hotel booking website.

The design should ideally be compatible with a content management system such as Page Loom. In terms of reference materials we like sites similar to:

http://www.velmarquay.net
http://www.corvidandpine.net
http://www.tessarooms.net
http://www.quillbeds.net

These sites are designed far more simply than large booking sites such as www.roamvix.net, www.bunkfold.net or even wander ledger. However, we are not looking for a copy of the above. We are looking for a design that presents hotels in a novel way and would be seen by the industry as a unique way of displaying new hotels.
Updates

Dear Designers - we have received quite a few entries already. Thank you. However, none of the designs submitted have responded to our brief. They are all copies or derivatives of current hotel websites which is not what we are looking for. We want (a) a new and creative approach to a hotel website and (b) one which creatively uses the age of the hotel (ie. 1 month old, 6 months old etc).

It will require creative thinking and new ideas. We wanted to challenge designers to come up with something new. Thanks.

```html
<!DOCTYPE html>
<html lang="en">
<head>
<meta charset="utf-8">
<title>Brindlestays – New Hotels</title>
<link href="https://fonts.googleapis.com/css2?family=Figtree:wght@400;600;700;800&family=Open+Sans:wght@400;700&display=swap" rel="stylesheet">
<style>
:root{
  --blue:#0a63b0;
  --ink:#2a2a2a;
  --nav:#6b6b6b;
  --muted:#a8a8a8;
  --tab-off:#cfcfcf;
  --link:#c0391b;
  --rule:#e4e4e4;
  --white:#ffffff;
}
*{margin:0;padding:0;box-sizing:border-box}
html,body{width:1200px;height:756px;overflow:hidden;background:var(--white)}
body{font-family:'Figtree',sans-serif;color:var(--ink);position:relative}

.site-header{position:absolute;left:0;top:0;width:1200px;height:62px;border-bottom:2px solid var(--rule)}
.brand{position:absolute;left:120px;top:16px;font-size:26px;font-weight:700;letter-spacing:-.5px;color:var(--ink)}
.main-nav{position:absolute;left:672px;top:17px;display:flex;align-items:center;height:26px}
.main-nav a{font-size:14px;color:var(--nav);text-decoration:none;padding:0 20px;line-height:26px}
.main-nav a.active{background:var(--blue);color:var(--white);
  clip-path:polygon(0 0,100% 0,96% 50%,100% 100%,0 100%,4% 50%)}
.share-btn{position:absolute;top:21px;height:19px;border:1px solid #bdbdbd;border-radius:3px;background:linear-gradient(#fafafa,#e2e2e2);font-size:11px;font-weight:700;color:#444;line-height:17px;padding:0 7px}
.header-share{left:994px}
.header-save{left:1050px}

.hero{position:absolute;left:0;top:63px;width:1200px;height:465px;
  background:
    radial-gradient(ellipse 260px 200px at 570px 120px,rgba(170,210,230,.95) 0%,rgba(140,175,195,.6) 45%,rgba(140,175,195,0) 100%),
    radial-gradient(ellipse 360px 200px at 200px 400px,rgba(235,215,190,.9) 0%,rgba(200,160,120,.5) 50%,rgba(200,160,120,0) 100%),
    linear-gradient(90deg,#6a5446 0%,#4a3a30 25%,#3a3632 50%,#4a4542 75%,#6e6c6a 100%)}
.hero-title{position:absolute;left:0;width:1200px;top:80px;text-align:center;font-size:34px;font-weight:800;color:var(--white);text-shadow:0 2px 8px rgba(0,0,0,.5)}
.hotel-badge{position:absolute;left:483px;top:141px;width:234px;height:234px;border-radius:50%;border:4px solid rgba(255,255,255,.8);background:rgba(10,10,10,.82);text-align:center;color:var(--white)}
.hotel-name{margin-top:50px;font-size:20px;font-weight:700;line-height:24px}
.badge-rule{display:block;margin:4px auto 6px}
.hotel-meta{font-size:15px;line-height:23px}
.arrow{position:absolute;top:164px}
.thumb-strip{position:absolute;left:346px;top:424px;width:509px;height:41px;background:var(--white);border-radius:24px 24px 0 0;display:flex;gap:6px;padding:5px 0 0 18px}
.thumb{width:42px;height:42px;border-radius:50%;flex:none}
.thumb.active{border:3px solid var(--blue)}

.tabs{position:absolute;left:435px;top:561px;display:flex;gap:10px}
.tab{height:26px;line-height:26px;font-size:17px;color:var(--white);text-align:center;
  clip-path:polygon(0 0,100% 0,97% 50%,100% 100%,0 100%,3% 50%)}
.tab-desc{width:123px;background:var(--blue)}
.tab-price{width:198px;background:var(--tab-off)}
.description{position:absolute;left:140px;top:596px;width:920px;text-align:center;font-family:'Open Sans',sans-serif;font-size:13px;line-height:15.5px;color:#3a3a3a}
.description strong{font-weight:700}
.actions{position:absolute;left:0;width:1200px;top:659px;display:flex;justify-content:center;align-items:center;gap:14px;padding-left:10px}
.visit-link{font-size:14px;color:var(--link);text-decoration:none}
.actions .share-btn{position:static}
.site-footer{position:absolute;left:0;top:706px;width:1200px;border-top:1px solid var(--rule);text-align:center;font-size:12px;color:var(--muted);padding-top:12px}
</style>
</head>
<body>
<header class="site-header">
  <div class="brand">BRINDLESTAYS</div>
  <nav class="main-nav">
    <a href="#">HOME</a>
    <a href="#" class="active">NEW HOTELS</a>
    <a href="#">ABOUT US</a>
  </nav>
  <span class="share-btn header-share">Share</span>
  <span class="share-btn header-save">Save</span>
</header>

<section class="hero" role="img" aria-label="Photo of a hotel bedroom with a bed, lamps and a city view through tall windows">
  <h1 class="hero-title">NEW HOTELS</h1>
  <svg class="arrow" style="left:96px" width="54" height="54" viewBox="0 0 54 54" aria-hidden="true">
    <circle cx="27" cy="27" r="27" fill="rgba(255,255,255,.45)"/>
    <path d="M31 16 L21 27 L31 38" fill="none" stroke="rgba(90,90,90,.8)" stroke-width="5"/>
  </svg>
  <svg class="arrow" style="left:1052px" width="54" height="54" viewBox="0 0 54 54" aria-hidden="true">
    <circle cx="27" cy="27" r="27" fill="rgba(255,255,255,.3)"/>
    <path d="M23 16 L33 27 L23 38" fill="none" stroke="rgba(255,255,255,.6)" stroke-width="5"/>
  </svg>
  <div class="hotel-badge">
    <div class="hotel-name">Harrow Quay<br>Hotel</div>
    <svg class="badge-rule" width="114" height="14" viewBox="0 0 114 14" aria-hidden="true">
      <line x1="0" y1="7" x2="114" y2="7" stroke="#3d6f9e" stroke-width="1"/>
      <circle cx="57" cy="7" r="6" fill="var(--blue)"/>
    </svg>
    <div class="hotel-meta">Age : 5 Months<br>Region : New York City<br>Reviews : 06</div>
  </div>
  <div class="thumb-strip">
    <div class="thumb active" role="img" aria-label="Bedroom photo" style="background:radial-gradient(circle at 60% 35%,#8fb4c8,#4a3a30 70%)"></div>
    <div class="thumb" role="img" aria-label="Terrace photo" style="background:radial-gradient(circle at 50% 30%,#c8b890,#6a5a40 75%)"></div>
    <div class="thumb" role="img" aria-label="Lobby photo" style="background:linear-gradient(#e6e6e6,#8a8a8a)"></div>
    <div class="thumb" role="img" aria-label="Pool photo" style="background:linear-gradient(#1a1a1a 30%,#2fb6c8 70%)"></div>
    <div class="thumb" role="img" aria-label="Tower photo" style="background:linear-gradient(#7fb2e6,#e8f0f6)"></div>
    <div class="thumb" role="img" aria-label="Beach photo" style="background:linear-gradient(#6f93b8,#b0b4b4)"></div>
    <div class="thumb" role="img" aria-label="Coast photo" style="background:linear-gradient(#e6f0f6,#c8905a)"></div>
    <div class="thumb" role="img" aria-label="Deck chairs photo" style="background:linear-gradient(#e0e4e8,#a86a3a)"></div>
    <div class="thumb" role="img" aria-label="Seaside photo" style="background:linear-gradient(#8fb0d8,#e8e8e8)"></div>
    <div class="thumb" role="img" aria-label="Pool photo" style="background:linear-gradient(#1a1a1a 30%,#2fb6c8 70%)"></div>
  </div>
</section>

<div class="tabs">
  <div class="tab tab-desc">Discription</div>
  <div class="tab tab-price">Feature Special Price</div>
</div>
<p class="description"><strong>Harrow Quay</strong> Lorem ipsum dolor sit amet, consectetur adipiscing elit. In fermentum dolor non augue egestas. Donec sem eros, tincidunt at congue ut, posuere sit amet est. Vivamus scelerisque viverra odio sit amet ut nec neque non justo rutrum tempor lobortis eu ante. Aliquam sagittis, nibh quis commodo auctor, risus mauris laoreet lectus, id facilisis libero odio nec enim. Sed id ligula adipiscing purus</p>
<div class="actions">
  <a href="#" class="visit-link">Click to visit website</a>
  <span class="share-btn">Share</span>
  <span class="share-btn">Save</span>
</div>
<footer class="site-footer">Contact - All right reserved © 2013 - Terms</footer>
</body>
</html>
```